Business Card Design

building company specialistloft conversion,extension ,bathrooms ,kitchens ,painting and decorating all general building work

Industry/Entity Type

Building

Contact Information for Business Card

K&R Home renewal Ltd
tel -07912468305
email-Rmarek07@brickmail.example
web in progres

Font styles to use
Sans Serif

Requirements
Must have
• name of the company
• all contact details
Nice to have
• some of the skills

```html
<!DOCTYPE html>
<html lang="en">
<head>
<meta charset="utf-8">
<title>Oakmere Builders Ltd – Business Card</title>
<link rel="stylesheet" href="https://fonts.googleapis.com/css2?family=Lato:wght@400;700&display=swap">
<style>
  :root {
    --page-bg: #e9e9e9;
    --card-white: #f8f8f8;
    --brand-orange: #ee9027;
    --ink-dark: #3a3a3a;
    --card-shadow: rgba(0, 0, 0, 0.16);
  }
  * { box-sizing: border-box; margin: 0; padding: 0; }
  html, body {
    width: 1200px;
    height: 900px;
    overflow: hidden;
    background: var(--page-bg);
    font-family: "Lato", sans-serif;
  }
  .canvas {
    position: relative;
    width: 1200px;
    height: 900px;
  }
  .card {
    position: absolute;
    width: 500px;
    height: 286px;
    border-radius: 3px;
    box-shadow: 0 10px 28px var(--card-shadow);
  }
  .card--front {
    left: 70px;
    top: 360px;
    background: var(--card-white);
  }
  .card--back {
    left: 630px;
    top: 254px;
    background: var(--brand-orange);
  }
  .holder {
    position: absolute;
    left: 34px;
    top: 30px;
  }
  .holder__name {
    color: var(--brand-orange);
    font-weight: 700;
    font-size: 19px;
    line-height: 1.1;
  }
  .holder__role {
    color: var(--ink-dark);
    font-size: 12px;
    margin-top: 3px;
  }
  .contact {
    position: absolute;
    left: 34px;
    top: 96px;
    list-style: none;
  }
  .contact__item { margin-bottom: 4px; }
  .contact__label {
    display: block;
    color: var(--brand-orange);
    font-size: 12px;
    line-height: 1.2;
  }
  .contact__value {
    display: block;
    color: var(--ink-dark);
    font-size: 13px;
    line-height: 1.25;
  }
  .brand {
    position: absolute;
    display: flex;
    align-items: center;
    gap: 10px;
    font-weight: 700;
    white-space: nowrap;
  }
  .brand__mark {
    width: 14px;
    height: 14px;
    flex: none;
  }
  .card--front .brand {
    right: 32px;
    top: 206px;
    color: var(--brand-orange);
    font-size: 22px;
  }
  .card--front .brand__mark { background: var(--ink-dark); }
  .card--back .brand {
    left: 50%;
    top: 50%;
    transform: translate(-50%, -50%);
    color: #ffffff;
    font-size: 32px;
  }
  .card--back .brand__mark { background: #ffffff; width: 18px; height: 18px; }
</style>
</head>
<body>
<main class="canvas">
  <section class="card card--front" aria-label="Business card front">
    <div class="holder">
      <p class="holder__name">Marek Rowan</p>
      <p class="holder__role">Managing Director</p>
    </div>
    <ul class="contact">
      <li class="contact__item">
        <span class="contact__label">telephone</span>
        <span class="contact__value">07700 900461</span>
      </li>
      <li class="contact__item">
        <span class="contact__label">email</span>
        <span class="contact__value">Rmarek07@brickmail.example</span>
      </li>
      <li class="contact__item">
        <span class="contact__label">address</span>
        <span class="contact__value">12 Station Road, Leeds, UK</span>
      </li>
    </ul>
    <div class="brand">
      <span class="brand__mark"></span>
      <span class="brand__name">Oakmere Builders Ltd</span>
    </div>
  </section>

  <section class="card card--back" aria-label="Business card back">
    <div class="brand">
      <span class="brand__mark"></span>
      <span class="brand__name">Oakmere Builders Ltd</span>
    </div>
  </section>
</main>
</body>
</html>
```